Business cards for a tribute and obituary website

Our website is called Tribute Lantern.

It is a special place online for people to remember their loved ones who have passed away, through obituaries and tributes. Friends and family can also convey their condolences on the deceased's memorial page. Celebrating the life of the deceased and remembering their legacy is very important to us – death should not be just about grieving.

We would like the card to look tasteful and modern. The design should ideally not have colours that are too bright. The logo and website URL, www.tributelantern.example should be visible on the front of the card, with our slogan "Celebrating a life passed" on the back.

The design should communicate our purpose – remembering loved ones who have passed – and also a lighter tone of celebrating life. It should not look like a funeral director's card!

Our logo has been attached. Looking forward to some beautiful designs! Get creative :)
Updates

Project Deadline Extended
Reason: Thank you all for your designs. The rest of my team and I have not reached a decision on which design to select and I am collecting feedback from them. I will provide feedback for any changes that need to be made soon. It would be great if we could see more original designs and in more colours! We will definitely select a design by this deadline.

Industry/Entity Type

Business

Contact Information for Business Card

Wendy Lumb
Project Manager
614772390
wendylumb@tributelantern.example

Font styles to use
Serif
Sans Serif

Requirements
Must have
• Logo and website address (www.tributelantern.example) on the front.
Nice to have
• Hi designers! It would be nice to see alternative colours – feel free to try out colours that are tasteful and subtle. The colour of the business card does not have to be the same as the logo.
• We would also like to see the logo used in different ways, perhaps a glossy or embossed finish. The card should look stylish.

```html
<!DOCTYPE html>
<html lang="en">
<head>
<meta charset="utf-8">
<title>Tribute Lantern – Business Cards</title>
<link href="https://fonts.googleapis.com/css2?family=Bitter:wght@700&family=Open+Sans:wght@400;600;700&display=swap" rel="stylesheet">
<style>
  :root {
    --page: #e9e6e1;
    --card-white: #ffffff;
    --card-black: #0e0e0e;
    --ink: #1a1a1a;
    --muted: #555555;
    --violet: #8a6cc0;
    --accent-red: #e8383d;
    --paper-white: #ffffff;
    --serif: 'Bitter', Georgia, serif;
    --sans: 'Open Sans', Arial, sans-serif;
  }
  * { margin: 0; padding: 0; box-sizing: border-box; }
  html, body {
    width: 1200px; height: 1023px; overflow: hidden;
    background: var(--page);
  }
  .sheet {
    width: 1200px; height: 1023px;
    display: flex; flex-direction: column; align-items: center; justify-content: center;
    gap: 40px;
  }
  .card {
    position: relative;
    width: 800px; height: 457px;
    border-radius: 26px;
    overflow: hidden;
    box-shadow: 0 6px 18px rgba(0,0,0,0.15);
  }
  .card--front { background: var(--card-white); }
  .card--back { background: var(--card-black); }

  .wordmark {
    display: flex; align-items: center; gap: 18px;
  }
  .wordmark__dot {
    width: 62px; height: 62px; border-radius: 50%;
  }
  .wordmark__name {
    font-family: var(--serif); font-weight: 700;
    font-size: 44px; line-height: 0.98;
  }

  .card--front .wordmark { position: absolute; left: 58px; top: 70px; }
  .card--front .wordmark__dot { background: var(--ink); }
  .card--front .wordmark__name { color: var(--ink); }

  .holder { position: absolute; left: 58px; top: 200px; }
  .holder__name {
    font-family: var(--sans); font-weight: 700; font-size: 27px;
    color: var(--violet); line-height: 1.1;
  }
  .holder__role {
    font-family: var(--sans); font-weight: 400; font-size: 19px;
    color: var(--muted); margin-top: 2px;
  }

  .contacts {
    position: absolute; left: 58px; top: 300px;
    list-style: none;
    font-family: var(--sans); font-size: 20px; color: var(--ink);
  }
  .contacts li { display: flex; align-items: center; gap: 10px; line-height: 34px; }
  .contacts svg { width: 16px; height: 16px; flex: none; }

  .card--back .wordmark { position: absolute; left: 70px; top: 70px; }
  .card--back .wordmark__dot { background: var(--paper-white); }
  .card--back .wordmark__name { color: var(--paper-white); font-size: 50px; }

  .tagline {
    position: absolute; right: 70px; bottom: 80px;
    font-family: var(--sans); font-weight: 700; font-size: 30px;
    color: var(--accent-red);
  }
</style>
</head>
<body>
<main class="sheet">
  <section class="card card--front" aria-label="Business card front">
    <div class="wordmark">
      <span class="wordmark__dot"></span>
      <span class="wordmark__name">Tribute<br>Lantern</span>
    </div>
    <div class="holder">
      <p class="holder__name">Wendy Lumb</p>
      <p class="holder__role">Project Manager</p>
    </div>
    <ul class="contacts">
      <li>
        <svg viewBox="0 0 16 16" aria-hidden="true"><path d="M4 1h3l1 4-2 1c1 2 2 3 4 4l1-2 4 1v3c0 1-1 2-2 2C7 14 2 9 2 3c0-1 1-2 2-2z" fill="#8a6cc0"/></svg>
        614772390
      </li>
      <li>
        <svg viewBox="0 0 16 16" aria-hidden="true"><rect x="1" y="1" width="14" height="14" rx="2" fill="#8a6cc0"/><path d="M4 8l3 3 5-6" stroke="#fff" stroke-width="2" fill="none"/></svg>
        wendylumb@tributelantern.example
      </li>
      <li>
        <svg viewBox="0 0 16 16" aria-hidden="true"><rect x="1.5" y="1.5" width="13" height="13" rx="2" fill="none" stroke="#555" stroke-width="1.5"/></svg>
        www.tributelantern.example
      </li>
    </ul>
  </section>

  <section class="card card--back" aria-label="Business card back">
    <div class="wordmark">
      <span class="wordmark__dot"></span>
      <span class="wordmark__name">Tribute<br>Lantern</span>
    </div>
    <p class="tagline">Celebrating a life passed</p>
  </section>
</main>
</body>
</html>
```